■依頼の目的/概要
ハルカゼのlumoraで電子書籍出版をします。

■本の内容
40代女性で話すことや伝えること
自分に自信はないけれど

起業したい、
夢や目標を叶えたい、
という方がターゲットです。

声と潜在意識(心)の力を使う「ひだまりトーン」で
人前で自信をもって伝えられるようになったり
やりたいことがどんどん実現できるようになる方法を
書きました。

声や潜在意識を使ったトレーニング、
実例を用いてお伝えしています。

■デザイン要望
40代女性が好むデザインが希望です。
顔写真も入れていただけたらと思います。
その際、手に持っている音符などは載せないようお願いいたします。

お写真と、電子書籍の文章をお送りいたします。

ご応募、心よりお待ちしております!!!

その他何かご不明な点がございましたら、お気軽にご質問下さい。
よろしくお願いいたします。
タイトルは
響きの名手がひもとく
輝く毎日をつくる心の整え方・磨き方
~ひだまりトーンの秘密~

著者は
ひだまりトーンコンサルタント
さとうれな

どうぞよろしくお願いいたします。
LQS表記では、表紙画像のサイズは 50 MB 未満表紙フ
ァイルの理想的な寸法は 2,560 x 1,600 ピクセルとなっています。

文字が見やすいこと。
女性的な優しいイメージと内容が合うもの、
という視点で選ばせていただきました。

素晴らしい作品ばかりで
選ばせていただくのに時間がかかりました。

短期間にも関わらず
素敵な作品を沢山ご応募いただき
どうもありがとうございました!

心より感謝いたします。

機会がございましたら
またどうぞよろしくお願いいたします。

```html
<!DOCTYPE html>
<html lang="ja">
<head>
<meta charset="UTF-8">
<title>輝く毎日をつくる心の整え方・磨き方</title>
<link href="https://fonts.googleapis.com/css2?family=Shippori+Mincho:wght@500;700&family=Noto+Serif+JP:wght@600;700&display=swap" rel="stylesheet">
<style>
  :root {
    --paper: #ffffff;
    --gold: #a58b68;
    --gold-deep: #8f7556;
    --band: #c987ad;
    --band-text: #ffffff;
    --leaf-tint: #eee3d3;
    --photo-a: #d9cfc6;
    --photo-b: #a89a90;
  }
  html, body { margin: 0; padding: 0; overflow: hidden; background: var(--paper); }
  .cover {
    position: relative;
    width: 750px;
    height: 1200px;
    background: var(--paper);
    overflow: hidden;
    font-family: "Shippori Mincho", "Noto Serif JP", serif;
  }
  .vertical {
    position: absolute;
    writing-mode: vertical-rl;
    color: var(--gold);
    white-space: nowrap;
    line-height: 1;
  }
  .title-lead {
    left: 552px; top: 36px;
    font-size: 32px; font-weight: 500;
    letter-spacing: 4px;
  }
  .title-main {
    left: 440px; top: 96px;
    font-size: 64px; font-weight: 700;
    color: var(--gold-deep);
    letter-spacing: 2px;
  }
  .subtitle {
    left: 364px; top: 110px;
    font-size: 40px; font-weight: 500;
    letter-spacing: 2px;
  }
  .leaf-ornament {
    position: absolute;
    left: 40px; top: 620px;
    width: 300px; height: 280px;
    border-radius: 50%;
    background: radial-gradient(ellipse at center, var(--leaf-tint) 0%, rgba(238,227,211,0) 70%);
  }
  .band {
    position: absolute;
    left: 0; top: 975px;
    width: 750px; height: 225px;
    background: var(--band);
  }
  .tagline {
    position: absolute;
    left: 38px; top: 1010px;
    margin: 0;
    color: var(--band-text);
    font-family: "Noto Serif JP", serif;
    font-weight: 700;
    font-size: 50px;
    line-height: 1.45;
    letter-spacing: 3px;
  }
  .author-photo {
    position: absolute;
    left: 470px; top: 790px;
    width: 240px; height: 240px;
    border-radius: 50%;
    border: 6px solid var(--paper);
    background: radial-gradient(circle at 50% 40%, var(--photo-a) 0%, var(--photo-b) 100%);
    box-sizing: border-box;
  }
  .author {
    position: absolute;
    left: 470px; top: 1128px;
    width: 250px;
    text-align: center;
    color: var(--band-text);
    font-family: "Noto Serif JP", serif;
    font-weight: 600;
  }
  .author-role { font-size: 15px; letter-spacing: 0.5px; display: block; }
  .author-name { font-size: 17px; letter-spacing: 2px; display: block; margin-top: 8px; }
</style>
</head>
<body>
<div class="cover">
  <div class="vertical title-lead">輝く毎日をつくる</div>
  <h1 class="vertical title-main" style="margin:0">心の整え方・磨き方</h1>
  <div class="vertical subtitle">～ひだまりトーンの秘密～</div>

  <div class="leaf-ornament" role="img" aria-label="金茶色の葉の枝の装飾"></div>

  <div class="band"></div>
  <p class="tagline">響きの名手が<br>ひもとく</p>

  <div class="author-photo" role="img" aria-label="著者の顔写真（円形）"></div>
  <div class="author">
    <span class="author-role">ひだまりトーンコンサルタント</span>
    <span class="author-name">さとうれな</span>
  </div>
</div>
</body>
</html>
```